Business Card Design

We need a new buisness card designed for a new company in Darwin
We dig trenchs and lay pipes for the communication industry,Electrical industry, Teleco industry,
We also do some concrete works as well,
And small excavation work
Communication
Belvanti Contracting PTY LTD
Pit and Pipe installations
Trenching,Excavations, Concreting ,
civil works, unistrut soloutions ,over thirty years experiance
WHERE NOT FAZED WE WILL LAY ANYTHING
Contact Glen 0491536208 ps
(would like name to stand out somehow in another text or graphic sort of a way am also looking for some sort of slogan) will most likely be a red card with black writing

```html
<!DOCTYPE html>
<html lang="en">
<head>
<meta charset="utf-8">
<title>Belvanti Contracting – Business Card</title>
<link rel="stylesheet" href="https://fonts.googleapis.com/css2?family=PT+Sans:ital,wght@0,400;0,700;1,700&display=swap">
<style>
  :root {
    --page-bg: #e9e7e4;
    --card-red: #e2292b;
    --card-red-deep: #cf1f22;
    --wave-white: #f7f7f7;
    --brand-blue: #5b5eae;
    --ink: #111111;
    --text-font: "PT Sans", sans-serif;
  }
  * { box-sizing: border-box; margin: 0; padding: 0; }
  html, body {
    width: 1200px; height: 1200px; overflow: hidden;
    background: var(--page-bg);
    font-family: var(--text-font);
  }
  .canvas {
    width: 1200px; height: 1200px;
    display: flex; align-items: center; justify-content: center;
  }
  .card {
    position: relative;
    width: 1050px; height: 600px;
    background: linear-gradient(160deg, var(--card-red) 0%, var(--card-red-deep) 100%);
    box-shadow: 0 12px 30px rgba(0,0,0,0.18);
    overflow: hidden;
    color: var(--ink);
  }
  .wave { position: absolute; inset: 0; width: 100%; height: 100%; }
  .brand {
    position: absolute; top: 50px; left: 270px;
    display: flex; align-items: center; gap: 26px;
  }
  .brand-dot {
    width: 96px; height: 96px; border-radius: 50%;
    background: var(--brand-blue);
  }
  .brand-divider { width: 3px; height: 110px; background: var(--brand-blue); }
  .brand-text { color: var(--brand-blue); font-weight: 700; line-height: 1; }
  .brand-name { font-size: 58px; letter-spacing: 2px; text-transform: uppercase; }
  .brand-legal { font-size: 33px; letter-spacing: 1px; text-transform: uppercase; margin-top: 4px; }
  .brand-tagline { font-size: 19px; letter-spacing: 0.5px; text-transform: uppercase; margin-top: 6px; }
  .contact {
    position: absolute; left: 90px; top: 300px;
    font-weight: 700; font-style: italic;
  }
  .contact-name { font-size: 32px; }
  .contact-phone { font-size: 30px; letter-spacing: 1px; margin-top: 6px; }
  .services {
    position: absolute; left: 500px; top: 298px;
    list-style: none; font-weight: 700; font-size: 36px;
  }
  .services li { display: flex; align-items: center; gap: 18px; height: 50px; }
  .services svg { width: 20px; height: 22px; flex: none; }
  .slogan {
    position: absolute; left: 0; right: 0; bottom: 30px;
    text-align: center; font-size: 25px; padding-right: 60px;
  }
</style>
</head>
<body>
<main class="canvas">
  <section class="card" aria-label="Belvanti Contracting business card">
    <svg class="wave" viewBox="0 0 1050 600" preserveAspectRatio="none" aria-hidden="true">
      <path d="M215,0 C245,120 340,175 520,178 C720,182 900,200 1050,285 L1050,0 Z" fill="var(--wave-white)"/>
    </svg>

    <header class="brand">
      <span class="brand-dot" aria-hidden="true"></span>
      <span class="brand-divider" aria-hidden="true"></span>
      <div class="brand-text">
        <div class="brand-name">Belvanti</div>
        <div class="brand-legal">Contracting PTY LTD</div>
        <div class="brand-tagline">Pit and Pipe Installation Specialist</div>
      </div>
    </header>

    <div class="contact">
      <p class="contact-name">Glen</p>
      <p class="contact-phone">Phone : 0491536208</p>
    </div>

    <ul class="services">
      <li><svg viewBox="0 0 20 22" aria-hidden="true"><path d="M2,2 L18,11 L2,20 L7,11 Z" fill="var(--ink)"/></svg>Trenching</li>
      <li><svg viewBox="0 0 20 22" aria-hidden="true"><path d="M2,2 L18,11 L2,20 L7,11 Z" fill="var(--ink)"/></svg>Excavations</li>
      <li><svg viewBox="0 0 20 22" aria-hidden="true"><path d="M2,2 L18,11 L2,20 L7,11 Z" fill="var(--ink)"/></svg>little bit of concreting</li>
    </ul>

    <p class="slogan">Where not fazed we will lay anything</p>
  </section>
</main>
</body>
</html>
```